Value-added components of an energy-as-a-service provider

BrightlyQ (www.brightlyq-example.com) is a turnkey energy solutions provider for educational institutions—which essentially means we can make recommendations for ways to improve heating, cooling, ventilation, lighting, building controls, etc., and then turn around and project-manage the implementation of these recommendations.Part of what makes us different than our competitors is recognizing the unique way that educational institutions make decisions: they employ a more collaborative approach, and given the 24/7 nature of school operations, any construction needs to be very carefully planned and communicated with building occupants.We are looking at competing in the "energy-as-a-service" (EaaS) field, which effectively capitalizes on the way institutions can self-supply energy. The biggest hurdles for most projects that either produce or conserve energy are (1) upfront cost (these projects are really expensive) and (2) implementation (full-time employees on campuses already have too much on their plates). What EaaS providers can do is alleviate these burdens by finding the capital to pay for equipment, which the school then repays through the associated energy savings. Providers also do the work of implementing the changes.BrightlyQ offers the same basic characteristics that other EaaS providers offer—but we have a few elements that are like the icing on the cake, or the cherry on top (insert your own dessert metaphor here). Namely, we work exclusively with schools and are familiar with that environment, know how to work around sensitive scheduling constraints, know how to engage stakeholders in an academic environment, etc. That's what we would like help with in a graphic. There's a couple of renderings we did in-house, but the feedback on the less crude one attached is that there's a bit too much emphasis on the three differentiating elements, and that it could be a bit more visually appealing. We're really open to suggestions here, but keeping it simple and classy is still paramount. Attached is the BrightlyQ brand standards guidebook, which has our color palette and fonts and such, and a couple of iterations of our logo are also attached.

```html
<!DOCTYPE html>
<html lang="en">
<head>
<meta charset="utf-8">
<title>BrightlyQ — Energy-as-a-Service Components</title>
<link rel="stylesheet" href="https://fonts.googleapis.com/css2?family=Prompt:wght@600&display=swap">
<style>
  :root {
    --bg: #ffffff;
    --pill: #e6e6e6;
    --pill-edge: #d4d4d4;
    --ink: #4a4a4a;
    --green: #6abf45;
    --navy: #1b3d73;
    --orange: #d06026;
    --teal: #4e7a87;
    --amber: #f6a41c;
    --badge: #d2d2d2;
  }
  html, body {
    margin: 0;
    padding: 0;
    width: 1200px;
    height: 709px;
    overflow: hidden;
    background: var(--bg);
  }
  .service-diagram {
    display: block;
    width: 1200px;
    height: 709px;
  }
  .label {
    font-family: "Prompt", sans-serif;
    font-weight: 600;
    font-size: 24px;
    fill: var(--ink);
    letter-spacing: 0.3px;
  }
  .pill { fill: var(--pill); stroke: var(--pill-edge); stroke-width: 1; }
  .ring-gap, .node-base { fill: #fff; }
  .brand-name {
    font-family: "Prompt", sans-serif;
    font-weight: 600;
    font-size: 20px;
    fill: var(--ink);
  }
</style>
</head>
<body>
<svg class="service-diagram" viewBox="0 0 1200 709" xmlns="http://www.w3.org/2000/svg" role="img" aria-label="BrightlyQ energy-as-a-service components: People, Process, Construction, Engineering, Financing, O&amp;M">
  <defs>
    <filter id="soft-shadow" x="-20%" y="-20%" width="140%" height="160%">
      <feDropShadow dx="0" dy="2" stdDeviation="2" flood-color="#000" flood-opacity="0.18"/>
    </filter>
  </defs>

  <!-- arch -->
  <g class="arch">
    <path style="fill:var(--navy)" d="M464,391 A142,142 0 0 1 606,249 L606,312 A79,79 0 0 0 527,391 Z"/>
    <path style="fill:var(--orange)" d="M747,391 A142,142 0 0 0 605,249 L605,312 A79,79 0 0 1 684,391 Z"/>
    <rect style="fill:var(--teal)" x="464" y="396" width="63" height="215"/>
    <rect style="fill:var(--amber)" x="685" y="396" width="62" height="215"/>
  </g>

  <!-- central brand badge -->
  <g class="brand-badge">
    <circle cx="606" cy="287" r="74" fill="#fff"/>
    <circle cx="606" cy="287" r="64" fill="var(--badge)" filter="url(#soft-shadow)"/>
    <text class="brand-name" x="606" y="294" text-anchor="middle">BrightlyQ</text>
  </g>

  <!-- people / process -->
  <g class="item item-top">
    <rect class="pill" x="430" y="108" width="355" height="63" rx="31.5" filter="url(#soft-shadow)"/>
    <text class="label" x="472" y="149">PEOPLE</text>
    <text class="label" x="654" y="149">PROCESS</text>
    <line x1="607" y1="170" x2="607" y2="210" stroke="var(--green)" stroke-width="8"/>
    <circle cx="607" cy="140" r="36" fill="var(--green)"/>
    <circle class="ring-gap" cx="607" cy="140" r="30"/>
    <circle cx="607" cy="140" r="25" fill="var(--green)"/>
    <circle class="node-base" cx="606" cy="214" r="17" filter="url(#soft-shadow)"/>
    <circle cx="606" cy="214" r="7.5" fill="var(--green)"/>
  </g>

  <!-- construction -->
  <g class="item item-construction">
    <rect class="pill" x="153" y="280" width="294" height="63" rx="31.5" filter="url(#soft-shadow)"/>
    <text class="label" x="172" y="320">CONSTRUCTION</text>
    <line x1="435" y1="316" x2="470" y2="326" stroke="var(--navy)" stroke-width="8"/>
    <circle cx="409" cy="311" r="36" fill="var(--navy)"/>
    <circle class="ring-gap" cx="409" cy="311" r="30"/>
    <circle cx="409" cy="311" r="25" fill="var(--navy)"/>
    <circle class="node-base" cx="480" cy="328" r="17" filter="url(#soft-shadow)"/>
    <circle cx="480" cy="328" r="7.5" fill="var(--navy)"/>
  </g>

  <!-- engineering -->
  <g class="item item-engineering">
    <rect class="pill" x="765" y="280" width="282" height="63" rx="31.5" filter="url(#soft-shadow)"/>
    <text class="label" x="848" y="320">ENGINEERING</text>
    <line x1="775" y1="316" x2="740" y2="326" stroke="var(--orange)" stroke-width="8"/>
    <circle cx="801" cy="311" r="36" fill="var(--orange)"/>
    <circle class="ring-gap" cx="801" cy="311" r="30"/>
    <circle cx="801" cy="311" r="25" fill="var(--orange)"/>
    <circle class="node-base" cx="731" cy="328" r="17" filter="url(#soft-shadow)"/>
    <circle cx="731" cy="328" r="7.5" fill="var(--orange)"/>
  </g>

  <!-- financing -->
  <g class="item item-financing">
    <rect class="pill" x="188" y="465" width="232" height="63" rx="31.5" filter="url(#soft-shadow)"/>
    <text class="label" x="209" y="505">FINANCING</text>
    <line x1="420" y1="496" x2="460" y2="496" stroke="var(--teal)" stroke-width="10"/>
    <circle cx="391" cy="497" r="36" fill="var(--teal)"/>
    <circle class="ring-gap" cx="391" cy="497" r="30"/>
    <circle cx="391" cy="497" r="25" fill="var(--teal)"/>
    <circle class="node-base" cx="464" cy="496" r="17" filter="url(#soft-shadow)"/>
    <circle cx="464" cy="496" r="7.5" fill="var(--teal)"/>
  </g>

  <!-- operations & maintenance -->
  <g class="item item-om">
    <rect class="pill" x="795" y="465" width="219" height="63" rx="31.5" filter="url(#soft-shadow)"/>
    <text class="label" x="877" y="505">O&amp;M</text>
    <line x1="750" y1="496" x2="795" y2="496" stroke="var(--amber)" stroke-width="10"/>
    <circle cx="822" cy="499" r="36" fill="var(--amber)"/>
    <circle class="ring-gap" cx="822" cy="499" r="30"/>
    <circle cx="822" cy="499" r="25" fill="var(--amber)"/>
    <circle class="node-base" cx="745" cy="496" r="17" filter="url(#soft-shadow)"/>
    <circle cx="745" cy="496" r="7.5" fill="var(--amber)"/>
  </g>
</svg>
</body>
</html>
```